Automotive Brand Survey Online

Hi guys, we are looking for a freelancer who can design User Interface design (UI) for a survey-online website layout. <br/><br/>For the content, there are question, choices, back and next buttons - as if you are designing a survey website.<br/><br/>There are 5 main contents of the website consists of:<br/>1. Single-answer question<br/>2. Yes/No-answer question<br/>3. Net Promoter Score (NPS) or 1-5 scale question<br/>4. Open-end question<br/>5. Thank you page when finish survey<br/><br/>Here is the demo and more description<br/>https://preview.quorvane.site/survey/
Target Market(s)
Car Owner
Industry/Entity Type
Automotive
Number of Pages Required
1 page

```html
<!DOCTYPE html>
<html lang="en">
<head>
<meta charset="utf-8">
<title>Survey Webpage Layout - Desktop</title>
<link href="https://fonts.googleapis.com/css2?family=Nunito+Sans:wght@400;600;700;800&display=swap" rel="stylesheet">
<style>
:root{
  --page-bg:#f6f6f7;
  --frame:#5a6079;
  --heading:#5a6280;
  --ink:#1c1c1c;
  --question:#1f3a5a;
  --green:#2f5a45;
  --track:#f1f1f1;
  --back:#8a1a1a;
  --footer-ink:#3a2a5a;
  --close:#9a2a3a;
  --orange:#fdb061;
  --orange-edge:#e6903a;
  --option-edge:#8f9399;
  --tint-1:#f2f2f2;
  --tint-2:#e9eaee;
  --tint-3:#f3eeea;
  --tint-4:#efeef1;
  --tint-5:#f2f2f2;
}
*{box-sizing:border-box;margin:0;padding:0}
html,body{width:1200px;height:3571px;overflow:hidden}
body{background:var(--page-bg);font-family:"Nunito Sans",Arial,sans-serif;position:relative;color:var(--ink)}
.page-title{position:absolute;left:0;width:1235px;top:40px;text-align:center;font-size:54px;font-weight:700;color:var(--heading);letter-spacing:2px}
.page-label{position:absolute;left:205px;font-size:21px;font-weight:700;color:var(--heading);letter-spacing:.5px}
.screen{position:absolute;left:198px;width:793px;height:549px;border:5px solid var(--frame);border-radius:24px;background:#fff;overflow:hidden}
.screen .backdrop{position:absolute;left:0;top:0;width:783px;height:539px}
.brand{position:absolute;left:36px;top:22px;display:flex;align-items:center;gap:8px;font-size:17px;font-weight:700;color:var(--heading)}
.brand-dot{width:16px;height:16px;border-radius:50%;background:var(--heading)}
.close{position:absolute;left:722px;top:30px;width:20px;height:20px}
.survey-title{position:absolute;left:0;width:783px;top:56px;text-align:center;font-size:24px;font-weight:700;letter-spacing:1.5px;color:var(--ink)}
.question{position:absolute;left:0;width:783px;top:112px;text-align:center;font-size:21px;font-weight:600;color:var(--question);letter-spacing:.4px}
.answer-box{position:absolute;left:157px;top:175px;width:469px;height:144px;border:1.5px solid var(--green);border-radius:8px;background:#fff}
.btn{position:absolute;width:95px;height:34px;border-radius:7px;background:var(--green);color:#fff;font-size:20px;font-weight:600;display:flex;align-items:center;justify-content:center}
.back{position:absolute;font-size:16px;font-weight:600;color:var(--back)}
.option{position:absolute;height:40px;border:1.5px solid var(--option-edge);border-radius:7px;background:#fff;font-size:14px;font-weight:600;color:var(--question);display:flex;align-items:center;padding-left:43px}
.option::before{content:"";position:absolute;left:14px;top:12px;width:14px;height:14px;border:1.5px solid var(--option-edge);border-radius:50%;box-sizing:border-box}
.option.selected{background:var(--green);border-color:var(--green);color:#fff}
.option.selected::before{border:3px solid #fff}
.option.centered{justify-content:center;padding-left:0}
.score{position:absolute;width:183px;height:40px;border:1.5px solid var(--option-edge);border-radius:7px;background:#fff;font-size:13px;color:var(--question);display:flex;align-items:center;justify-content:center}
.score.selected{background:var(--orange);border-color:var(--orange-edge);color:#fff}
.thanks{position:absolute;left:0;width:793px;top:220px;text-align:center;font-size:35px;font-weight:600;color:#2b4561;letter-spacing:.5px}
.progress-label{position:absolute;left:42px;font-size:16px;font-weight:700;color:var(--ink)}
.progress-track{position:absolute;left:40px;width:696px;height:28px;border-radius:8px;background:var(--track);overflow:hidden}
.progress-fill{height:100%;border-radius:8px;background:var(--green);color:#fff;font-size:14px;font-weight:600;display:flex;align-items:center;justify-content:center}
.footer{position:absolute;left:0;right:0;bottom:0;height:30px;display:flex;justify-content:space-between;align-items:center;padding:0 44px 0 40px;font-size:9.5px;font-weight:700;color:var(--footer-ink)}
</style>
</head>
<body>

<h1 class="page-title">Survey Webpage Layout - Desktop</h1>

<!-- Screen 1: open-end question -->
<div class="page-label" style="top:156px">Page - 1</div>
<section class="screen" style="top:202px">
  <svg class="backdrop" viewBox="0 0 783 539" aria-hidden="true"><path d="M0 0H783V85C650 160 480 230 392 355C304 230 133 160 0 85Z" fill="var(--tint-1)"/></svg>
  <div class="brand"><span class="brand-dot"></span>Korvane</div>
  <svg class="close" viewBox="0 0 20 20" aria-hidden="true"><circle cx="10" cy="10" r="8" fill="none" stroke="var(--close)" stroke-width="1.5"/><path d="M6.5 6.5L13.5 13.5M13.5 6.5L6.5 13.5" stroke="var(--close)" stroke-width="1.5"/></svg>
  <h2 class="survey-title">CUSTOMER SURVEY</h2>
  <p class="question">How do you feel with this car model?</p>
  <div class="answer-box"></div>
  <div class="btn" style="left:344px;top:368px">Next</div>
  <div class="progress-label" style="top:421px">Progress Bar</div>
  <div class="progress-track" style="top:446px"></div>
  <div class="footer" style="background:#fff"><span>Terms of Service and Privacy Policy</span><span>@2020</span></div>
</section>

<!-- Screen 2: single answer -->
<div class="page-label" style="top:812px">Page - 2</div>
<section class="screen" style="top:859px">
  <svg class="backdrop" viewBox="0 0 783 539" aria-hidden="true"><path d="M0 0H783V85C650 160 480 230 392 355C304 230 133 160 0 85Z" fill="var(--tint-2)"/></svg>
  <div class="brand"><span class="brand-dot"></span>Korvane</div>
  <svg class="close" viewBox="0 0 20 20" aria-hidden="true"><circle cx="10" cy="10" r="8" fill="none" stroke="var(--close)" stroke-width="1.5"/><path d="M6.5 6.5L13.5 13.5M13.5 6.5L6.5 13.5" stroke="var(--close)" stroke-width="1.5"/></svg>
  <h2 class="survey-title">CUSTOMER SURVEY</h2>
  <p class="question">Which car model you purchased in the past year?</p>
  <div class="option" style="left:182px;top:164px;width:183px">Aster Mini</div>
  <div class="option selected" style="left:409px;top:164px;width:183px">Velmont S2</div>
  <div class="option" style="left:182px;top:224px;width:183px">Korvane 2</div>
  <div class="option" style="left:409px;top:224px;width:183px">Lunor RX3</div>
  <div class="option" style="left:182px;top:283px;width:183px">Velmont C3</div>
  <div class="option" style="left:409px;top:283px;width:183px">Others</div>
  <div class="back" style="left:314px;top:378px">Back</div>
  <div class="btn" style="left:419px;top:368px">Next</div>
  <div class="progress-label" style="top:421px">Progress Bar</div>
  <div class="progress-track" style="top:446px"><div class="progress-fill" style="width:25%">25%</div></div>
  <div class="footer" style="background:var(--tint-2)"><span>Terms of Service and Privacy Policy</span><span>@2020</span></div>
</section>

<!-- Screen 3: yes / no -->
<div class="page-label" style="top:1471px">Page - 3</div>
<section class="screen" style="top:1523px">
  <svg class="backdrop" viewBox="0 0 783 539" aria-hidden="true"><path d="M0 0H783V85C650 160 480 230 392 355C304 230 133 160 0 85Z" fill="var(--tint-3)"/></svg>
  <div class="brand"><span class="brand-dot"></span>Korvane</div>
  <svg class="close" viewBox="0 0 20 20" aria-hidden="true"><circle cx="10" cy="10" r="8" fill="none" stroke="var(--close)" stroke-width="1.5"/><path d="M6.5 6.5L13.5 13.5M13.5 6.5L6.5 13.5" stroke="var(--close)" stroke-width="1.5"/></svg>
  <h2 class="survey-title">CUSTOMER SURVEY</h2>
  <p class="question">Do you own any car?</p>
  <div class="option selected centered" style="left:294px;top:189px;width:183px">YES</div>
  <div class="option centered" style="left:294px;top:247px;width:183px">NO</div>
  <div class="back" style="left:314px;top:378px">Back</div>
  <div class="btn" style="left:419px;top:368px">Next</div>
  <div class="progress-label" style="top:421px">Progress Bar</div>
  <div class="progress-track" style="top:446px"><div class="progress-fill" style="width:51%">50%</div></div>
  <div class="footer" style="background:var(--tint-3)"><span>Terms of Service and Privacy Policy</span><span>@2020</span></div>
</section>

<!-- Screen 4: satisfaction scale -->
<div class="page-label" style="top:2139px">Page - 4</div>
<section class="screen" style="top:2197px">
  <svg class="backdrop" viewBox="0 0 783 539" aria-hidden="true"><path d="M0 0H783V85C650 160 480 230 392 355C304 230 133 160 0 85Z" fill="var(--tint-4)"/></svg>
  <div class="brand"><span class="brand-dot"></span>Korvane</div>
  <svg class="close" viewBox="0 0 20 20" aria-hidden="true"><circle cx="10" cy="10" r="8" fill="none" stroke="var(--close)" stroke-width="1.5"/><path d="M6.5 6.5L13.5 13.5M13.5 6.5L6.5 13.5" stroke="var(--close)" stroke-width="1.5"/></svg>
  <h2 class="survey-title">CUSTOMER SURVEY</h2>
  <p class="question">Please rate your satisfaction score.</p>
  <div class="score" style="left:78px;top:183px">5</div>
  <div class="score" style="left:296px;top:183px">4</div>
  <div class="score selected" style="left:513px;top:183px">3</div>
  <div class="score" style="left:186px;top:253px">2</div>
  <div class="score" style="left:408px;top:253px">1</div>
  <div class="back" style="left:314px;top:378px">Back</div>
  <div class="btn" style="left:419px;top:368px">Done</div>
  <div class="progress-label" style="top:421px">Progress Bar</div>
  <div class="progress-track" style="top:446px"><div class="progress-fill" style="width:75%">75%</div></div>
  <div class="footer" style="background:var(--tint-4)"><span>Terms of Service and Privacy Policy</span><span>@2020</span></div>
</section>

<!-- Screen 5: thank you -->
<div class="page-label" style="top:2816px">Page - 5</div>
<section class="screen" style="top:2866px">
  <svg class="backdrop" viewBox="0 0 783 539" aria-hidden="true"><path d="M0 0H783V85C650 160 480 230 392 355C304 230 133 160 0 85Z" fill="var(--tint-5)"/></svg>
  <div class="brand"><span class="brand-dot"></span>Korvane</div>
  <svg class="close" viewBox="0 0 20 20" aria-hidden="true"><circle cx="10" cy="10" r="8" fill="none" stroke="var(--close)" stroke-width="1.5"/><path d="M6.5 6.5L13.5 13.5M13.5 6.5L6.5 13.5" stroke="var(--close)" stroke-width="1.5"/></svg>
  <h2 class="survey-title">CUSTOMER SURVEY</h2>
  <p class="thanks">Thanks for you Survey !</p>
  <div class="progress-label" style="top:421px">Progress Bar</div>
  <div class="progress-track" style="top:446px"><div class="progress-fill" style="width:100%">100%</div></div>
  <div class="footer" style="background:var(--tint-5)"><span>Terms of Service and Privacy Policy</span><span>@2020</span></div>
</section>

</body>
</html>
```